TRU PEAK POWER.

I'd like my business logo.
contact name: Desmond Halvik
phone:0438275160
email: info@trupeakpower.net.au
website: www.trupeakpower.net.au

services:
solar
battery storage
LED lighting
energy saving solutions
general electrical
I'd like the design to look professional

Target Market(s)

Everyone

Industry/Entity Type

Business

Contact Information for Business Card

as described above

Requirements
Must have
• Id like the colours and the design to work well with my logo.

```html
<!DOCTYPE html>
<html lang="en">
<head>
<meta charset="utf-8">
<title>Tru Peak Power – Business Card</title>
<link rel="stylesheet" href="https://fonts.googleapis.com/css2?family=Roboto+Condensed:wght@700&family=Arimo:wght@400;700&display=swap">
<style>
  :root {
    --page-bg: #eeeeec;
    --card-bg: #ffffff;
    --green-dark: #3f6f2a;
    --green-text: #3d6b24;
    --green-light: #7dc242;
    --yellow: #f7c400;
    --sun: #f5a91b;
    --ink: #1d1d1b;
    --white: #ffffff;
  }
  * { box-sizing: border-box; margin: 0; padding: 0; }
  html, body {
    width: 1200px;
    height: 786px;
    overflow: hidden;
    background: var(--page-bg);
  }
  .card {
    position: absolute;
    left: 80px;
    top: 75px;
    width: 1040px;
    height: 636px;
    background: var(--card-bg);
    box-shadow: 0 6px 22px rgba(0,0,0,0.12);
    overflow: hidden;
  }
  .card__bands {
    position: absolute;
    left: 0;
    top: 0;
    width: 1040px;
    height: 636px;
  }
  .brand {
    position: absolute;
    left: 156px;
    top: 60px;
    width: 740px;
    height: 190px;
    display: flex;
    align-items: center;
    gap: 34px;
  }
  .brand__mark {
    width: 150px;
    height: 150px;
    border-radius: 50%;
    background: var(--sun);
    flex: none;
  }
  .brand__name {
    font-family: "Roboto Condensed", "Arial Narrow", sans-serif;
    font-weight: 700;
    font-size: 76px;
    letter-spacing: 1px;
    color: var(--green-text);
    white-space: nowrap;
  }
  .services {
    position: absolute;
    left: 62px;
    top: 338px;
    width: 920px;
    font-family: "Roboto Condensed", "Arial Narrow", sans-serif;
    font-weight: 700;
    font-size: 22.5px;
    line-height: 30px;
    color: var(--green-text);
    white-space: nowrap;
  }
  .contacts {
    position: absolute;
    left: 62px;
    top: 394px;
    list-style: none;
    font-family: "Arimo", Arial, sans-serif;
    font-size: 21px;
    color: var(--white);
  }
  .contacts__item {
    display: flex;
    align-items: center;
    height: 32px;
    margin-bottom: 14px;
  }
  .contacts__item:nth-child(2) { margin-bottom: 11px; }
  .contacts__icon {
    width: 32px;
    height: 32px;
    margin-right: 16px;
    background: var(--green-light);
    color: var(--white);
    font-size: 16px;
    font-weight: 700;
    display: flex;
    align-items: center;
    justify-content: center;
  }
  .contact-name {
    position: absolute;
    left: 544px;
    top: 438px;
    width: 400px;
    text-align: center;
    font-family: "Arimo", Arial, sans-serif;
    font-weight: 700;
    font-size: 30px;
    line-height: 40px;
    color: var(--ink);
  }
</style>
</head>
<body>
  <main class="card">
    <svg class="card__bands" viewBox="0 0 1040 636" aria-hidden="true">
      <polygon points="0,375 437,375 523,538 0,538" fill="var(--green-dark)"/>
      <polygon points="452,375 1040,375 1040,538 536,538" fill="var(--yellow)"/>
      <rect x="0" y="548" width="1040" height="30" fill="var(--green-dark)"/>
      <rect x="0" y="578" width="1040" height="26" fill="var(--yellow)"/>
      <rect x="0" y="604" width="1040" height="32" fill="var(--green-dark)"/>
    </svg>

    <header class="brand">
      <span class="brand__mark" aria-hidden="true"></span>
      <h1 class="brand__name">TRU PEAK POWER</h1>
    </header>

    <p class="services">SOLAR BATTERY STORAGE, LED LIGHTING, ENERGY SAVING SOLUTIONS, GENERAL ELECTRICAL</p>

    <ul class="contacts">
      <li class="contacts__item"><span class="contacts__icon">P</span>0438275160</li>
      <li class="contacts__item"><span class="contacts__icon">e</span>info@trupeakpower.net.au</li>
      <li class="contacts__item"><span class="contacts__icon">w</span>www.trupeakpower.net.au</li>
    </ul>

    <p class="contact-name">Desmond Halvik</p>
  </main>
</body>
</html>
```